BQ PowerPoint Template Refresh

I'm looking to refresh our corporate presentation collateral, namely our base PowerPoint template. I need something that sparks, and gives the appearance of our contemporary firm that is hip, innovative, and modern. The project should provide for the various slide master templates with appropriately sized background images for slides in 4:3 and 16:9 formats

Target Market(s)

Investment banking prospect and clients which are typically in the high-tech industries of software, semiconductors,telecom, and telecom components

Industry/Entity Type

Investment Banking

Font styles to use
Other font styles liked:
• Goudy Old Style

Requirements
Must have
• - Must leverage current logo (red color is the standard, however portions of the logo or, color variations from our stock are possible for use), primary and secondary current colors. Non-section text is Goudy Old Style (headers and body text)
- The PPT template must have at least all of the LAYOUT options found in the Old BQ Prez
- Options with and without the Brixley logo as a transparent background
- Need a final version in 16:9 and 4:3 formats
- Must be able to add footer information such as "Confidential Information", slide number, and date
Nice to have
• a few design ideas on the IP Engineering image found on slide 7 of the New BQ Prez Attempt.ppt file

```html
<!DOCTYPE html>
<html lang="en">
<head>
<meta charset="utf-8">
<title>Brixley Advisors – Presentation Template</title>
<link href="https://fonts.googleapis.com/css2?family=Open+Sans:ital,wght@0,400;0,600;0,700;1,400&display=swap" rel="stylesheet">
<style>
:root{
  --red:#d92b2f;
  --navy:#1d3b70;
  --blue:#3f86d0;
  --grey-bg:#a6a6a6;
  --grey-row:#d4d6d8;
  --grey-num:#7c8790;
  --ink:#2b2b2b;
  --soft:#f7dede;
  --photo:#b9bcbf;
}
*{box-sizing:border-box;margin:0;padding:0}
html,body{width:1200px;height:960px;overflow:hidden}
body{background:var(--grey-bg);font-family:"Open Sans",Arial,sans-serif;color:var(--ink);position:relative}
.slide{position:absolute;width:353px;height:199px;background:#fff;overflow:hidden;box-shadow:0 1px 4px rgba(0,0,0,.25)}
.c1{left:50px}.c2{left:429px}.c3{left:799px}
.r1{top:54px}.r2{top:274px}.r3{top:502px}.r4{top:725px}
.deco{position:absolute;right:-30px;top:70px;width:120px;height:120px;border-radius:50%;background:var(--soft);opacity:.6}
.tag{position:absolute;left:14px;top:0;width:16px;height:10px;background:var(--red)}
.title{position:absolute;left:14px;top:13px;font-size:10.5px;font-weight:600;color:var(--navy);line-height:1.1}
.sub{position:absolute;left:14px;top:25px;font-size:7px;color:#222}
.brand{position:absolute;left:18px;bottom:10px;display:flex;align-items:center;gap:3px;color:var(--red);font-size:8px;font-weight:600;letter-spacing:.3px}
.brand i{display:block;width:11px;height:11px;border-radius:50%;background:var(--red)}
.rule{position:absolute;left:82px;right:28px;bottom:15px;height:1px;background:#c9c9c9}
.page{position:absolute;right:12px;bottom:9px;width:13px;height:13px;border-radius:50%;background:var(--red);color:#fff;font-size:5px;display:flex;align-items:center;justify-content:center}
.txt{position:absolute;font-size:4.3px;line-height:1.75;color:var(--ink)}
.txt em{display:block;font-style:italic;color:#444}
.txt em.blue{color:var(--navy)}
.ph{position:absolute;background:linear-gradient(160deg,#d8dadc,var(--photo) 60%,#8e9398)}
/* cover */
.cover{background:var(--red);color:#fff}
.cover .logo{position:absolute;left:22px;top:22px;display:flex;align-items:center;gap:5px;font-size:17px;font-weight:400;letter-spacing:1px}
.cover .logo i{width:26px;height:26px;border-radius:50%;background:#fff}
.cover .logo small{display:block;font-size:6px;letter-spacing:4px}
.cover .bar{position:absolute;right:22px;top:104px;width:58px;height:3px;background:#fff}
.cover h1{position:absolute;right:19px;top:118px;text-align:right;font-weight:400;font-size:15px;line-height:1.3}
.cover p{position:absolute;right:19px;top:166px;font-size:6.5px}
/* steps */
.steps-title{position:absolute;left:38px;top:80px;text-align:right;font-size:9.5px;font-weight:600;color:var(--navy);line-height:1.55}
.vline{position:absolute;left:104px;top:18px;height:152px;width:1px;background:#9aa2a8}
.step{position:absolute;left:104px;display:flex;gap:8px}
.num{width:26px;height:26px;border-radius:50%;background:var(--grey-num);border:2px solid #fff;box-shadow:0 0 0 1px var(--grey-num);color:#fff;font-size:13px;display:flex;align-items:center;justify-content:center;flex:none}
.step div.t{font-size:4.3px;line-height:1.6;width:178px}
.step b{font-size:5.4px;font-weight:600;display:block}
/* band */
.band{position:absolute;left:0;right:0;top:68px;height:26px;background:var(--navy)}
.col3{position:absolute;top:74px;width:90px;text-align:center}
.col3 .n{margin:0 auto;width:26px;height:26px;border-radius:50%;background:#2b2f36;border:2px solid #fff;color:#fff;font-size:11px;display:flex;align-items:center;justify-content:center}
.col3 h4{font-size:4.8px;font-weight:600;margin:5px 0 4px}
.col3 p{font-size:4px;line-height:1.7;text-align:left}
/* table */
table{position:absolute;left:14px;top:81px;width:322px;border-collapse:separate;border-spacing:4px 3px;font-size:6.5px}
th{background:var(--navy);color:#fff;font-weight:600;height:11px}
td{background:var(--grey-row);height:11px;padding-left:8px}
td.c{text-align:center;padding:0}
td.b{font-weight:600}
/* closing */
.close-band{position:absolute;left:0;right:0;top:129px;height:70px;background:var(--red);color:#fff}
.close-band .brand{color:#fff;left:20px;bottom:28px;font-size:10px}
.close-band .brand i{background:#fff;width:15px;height:15px}
.close-band .sep{position:absolute;left:95px;top:18px;width:1px;height:36px;background:#fff}
.close-band .info{position:absolute;left:99px;top:18px;font-size:4.6px;line-height:1.55}
</style>
</head>
<body>

<!-- Cover -->
<section class="slide cover c1 r1">
  <div class="logo"><i></i><div>BRIXLEY<small>ADVISORS</small></div></div>
  <div class="bar"></div>
  <h1>YOUR HEADLINE TEXT<br>HERE TO PUT</h1>
  <p>LOREM IPSUM IS SIMPLY DUMMY HAS BEEN</p>
</section>

<!-- Four steps -->
<section class="slide c2 r1">
  <div class="deco"></div>
  <div class="steps-title">YOUR<br>HEADLINE<br>HERE</div>
  <div class="vline"></div>
  <div class="step" style="top:20px;left:104px;margin-left:-13px"><div class="num">1</div><div class="t"><b>Tallyra builds automation in stages</b>System reaches full automation with Tallyra AI. It automates routine tasks so users can work smoothly, and grows into a trusted advisor over time for all their accounting needs.</div></div>
  <div class="step" style="top:61px;left:91px"><div class="num">2</div><div class="t"><b>Tallyra builds automation in stages</b>System reaches full automation with Tallyra AI. It automates routine tasks so users can work smoothly, and grows into a trusted advisor over time for all their accounting needs.</div></div>
  <div class="step" style="top:103px;left:91px"><div class="num">3</div><div class="t"><b>Tallyra builds automation in stages</b>System reaches full automation with Tallyra AI. It automates routine tasks so users can work smoothly, and grows into a trusted advisor over time for all their accounting needs.</div></div>
  <div class="step" style="top:144px;left:91px"><div class="num">4</div><div class="t"><b>Tallyra builds automation in stages</b>System reaches full automation with Tallyra AI. It automates routine tasks so users can work smoothly, and grows into a trusted advisor over time for all their accounting needs.</div></div>
  <div class="brand"><i></i>BRIXLEY</div><div class="rule"></div><div class="page">12</div>
</section>

<!-- Text only -->
<section class="slide c3 r1">
  <div class="deco"></div>
  <div class="tag"></div><h2 class="title">YOUR HEADLINE HERE</h2><p class="sub">Lorem ipsum is simply dummy has been</p>
  <div class="txt" style="left:18px;top:45px;width:322px">
    <em>AI automated accounting</em>
    Tallyra builds automation in stages on top of its current system to reach full automation thanks to Tallyra AI. Tallyra AI automates every manual task performed by the user. It starts by connecting to all sources of accounting data such as bank accounts, credit cards, webshops or document storage (Boxwell or Vaultly). Based on this data, Tallyra AI creates bookings and generates financial reports. Finally, its chat-like interface lets users communicate smoothly, so it acts as a trusted advisor over time.
    <em style="margin-top:3px">Blockchain software license or Token-as-a-License (TaaL)</em>
    It is possible to create tokens on a blockchain that represent software licenses, also known as Token-as-a-License (TaaL). Tallyra creates TaaL by using the Kestrel wallet, which interacts with the Kestrel blockchain. Once purchased, the holder is free to transfer or sell the TaaL on a secondary market built directly over the blockchain. Tallyra checks the validity of a token against the chain, so only token holders gain access. It also makes distribution and resale easier for developers and owners alike.
  </div>
  <div class="brand"><i></i>BRIXLEY</div><div class="rule"></div><div class="page">12</div>
</section>

<!-- Two columns -->
<section class="slide c1 r2">
  <div class="deco"></div>
  <div class="tag"></div><h2 class="title">YOUR HEADLINE HERE</h2><p class="sub">Lorem ipsum is simply dummy has been</p>
  <div class="txt" style="left:16px;top:53px;width:158px">
    <em>AI automated accounting</em>
    Tallyra builds automation in stages on top of its current system to reach full automation thanks to Tallyra AI. It automates every manual task performed by the user. It starts by connecting to all sources of accounting data such as bank accounts, credit cards, webshops or document storage (Boxwell or Vaultly). Based on this data, Tallyra AI creates bookings and financial reports. Finally, a chat-like interface lets users communicate smoothly, and it becomes a trusted advisor over time. It also makes license management and resale easier for software developers.
  </div>
  <div class="txt" style="left:182px;top:53px;width:158px">
    <em>Blockchain software license or Token-as-a-License</em>
    It is possible to create tokens on a blockchain that represent software licenses, also known as Token-as-a-License (TaaL). Tallyra creates TaaL by using the Kestrel wallet, which interacts with the Kestrel blockchain. Once purchased, the holder is free to transfer or sell the TaaL on a secondary market built directly over the blockchain. Tallyra checks the validity of a token against the chain, ensuring only holders have access to the software. It also makes distribution and resale of licenses easier for developers and owners.
  </div>
  <div class="brand"><i></i>BRIXLEY</div><div class="rule"></div><div class="page">12</div>
</section>

<!-- Image placeholder -->
<section class="slide c2 r2">
  <div class="deco"></div>
  <div class="tag"></div><h2 class="title">YOUR HEADLINE HERE</h2><p class="sub">Lorem ipsum is simply dummy has been</p>
  <div style="position:absolute;left:16px;top:55px;width:160px;height:112px;background:#6a6a6a;color:#e8e8e8;font-size:15px;display:flex;align-items:center;justify-content:center">Image</div>
  <div class="txt" style="left:180px;top:53px;width:160px">
    All in all, TaaL has a higher <i>value as a normal software license.</i>
    <em>Blockchain software license or Token-as-a-License</em>
    It is possible to create tokens on a blockchain that represent software licenses, also known as Token-as-a-License (TaaL). Tallyra creates TaaL by using the Kestrel wallet, which interacts with the Kestrel blockchain. Once purchased, the holder is free to transfer or sell the TaaL on a secondary market built over the blockchain, in our case the Kestrel marketplace. Tallyra checks the validity of a token against the chain, so only holders have access to the software. TaaL makes distribution and resale of licenses easier for developers.
  </div>
  <div class="brand"><i></i>BRIXLEY</div><div class="rule"></div><div class="page">12</div>
</section>

<!-- Photo left -->
<section class="slide c3 r2">
  <div class="deco"></div>
  <div class="tag"></div><h2 class="title">YOUR HEADLINE HERE</h2><p class="sub">Lorem ipsum is simply dummy has been</p>
  <div class="ph" role="img" aria-label="Photo of a businessman standing in a bright modern office" style="left:14px;top:46px;width:95px;height:108px"></div>
  <div class="txt" style="left:121px;top:47px;width:222px">
    <em>AI automated accounting</em>
    Tallyra builds automation in stages on top of its current system to reach full automation thanks to Tallyra AI. It automates every manual task performed by the user. It starts by connecting to all sources of accounting data such as bank accounts, credit cards, webshops or document storage (Boxwell or Vaultly). Based on this data, it creates bookings and generates financial reports. Finally, a chat-like interface lets users communicate smoothly, so it acts as a trusted advisor. It also makes license management and resale easier for software developers and owners. All in all, TaaL has a higher value as a normal software license.
    <em class="blue">Blockchain software license or Token-as-a-License</em>
    It is possible to create tokens on a blockchain that represent software licenses, also known as Token-as-a-License (TaaL). Tallyra creates TaaL by using the Kestrel wallet.
  </div>
  <div class="brand"><i></i>BRIXLEY</div><div class="rule"></div><div class="page">12</div>
</section>

<!-- Two photos with captions -->
<section class="slide c1 r3">
  <div class="deco"></div>
  <div class="tag"></div><h2 class="title">YOUR HEADLINE HERE</h2><p class="sub">Lorem ipsum is simply dummy has been</p>
  <div class="ph" role="img" aria-label="Photo of a business team walking together" style="left:14px;top:46px;width:77px;height:108px"></div>
  <div class="txt" style="left:95px;top:44px;width:78px">AI automated accounting<br>Tallyra builds automation in stages on top of its current system to reach full automation thanks to Tallyra AI. It automates every manual task performed by the user. It starts by connecting to all sources of accounting data such as bank accounts, credit cards, webshops or document storage (Boxwell or Vaultly). Based on this data,</div>
  <div class="ph" role="img" aria-label="Photo of a business team walking together" style="left:179px;top:46px;width:77px;height:108px"></div>
  <div class="txt" style="left:260px;top:44px;width:78px">AI automated accounting<br>Tallyra builds automation in stages on top of its current system to reach full automation thanks to Tallyra AI. It automates every manual task performed by the user. It starts by connecting to all sources of accounting data such as bank accounts, credit cards, webshops or document storage (Boxwell or Vaultly). Based on this data,</div>
  <div class="brand"><i></i>BRIXLEY</div><div class="rule"></div><div class="page">12</div>
</section>

<!-- Wide photo -->
<section class="slide c2 r3">
  <div class="deco"></div>
  <div class="tag"></div><h2 class="title">YOUR HEADLINE HERE</h2><p class="sub">Lorem ipsum is simply dummy has been</p>
  <div class="ph" role="img" aria-label="Photo of colleagues walking through a modern office" style="left:14px;top:47px;width:170px;height:107px"></div>
  <div class="txt" style="left:196px;top:45px;width:148px">
    <em>AI automated accounting</em>
    Tallyra builds automation in stages on top of its current system to reach full automation thanks to Tallyra AI. It automates every manual task performed by the user. It starts by connecting to all sources of accounting data such as bank accounts, credit cards, webshops or document storage (Boxwell or Vaultly). Based on this data, Tallyra AI creates bookings and generates financial reports. Finally, a chat-like interface lets users communicate smoothly, and it acts as a trusted advisor over time for all their accounting queries. It also makes license management and resale easier.
  </div>
  <div class="brand"><i></i>BRIXLEY</div><div class="rule"></div><div class="page">12</div>
</section>

<!-- Three steps band -->
<section class="slide c3 r3">
  <div class="tag"></div><h2 class="title">YOUR HEADLINE HERE</h2><p class="sub">Lorem ipsum is simply dummy has been</p>
  <div class="txt" style="left:20px;top:47px;width:316px;font-size:4px;line-height:1.6">Tallyra builds automation in stages on top of its current system to reach full automation thanks to Tallyra AI. It automates every manual task performed by the user, starting with all sources of accounting data such as bank accounts and webshops.</div>
  <div class="band"></div>
  <div class="col3" style="left:18px"><div class="n">1</div><h4>Tallyra builds</h4><p>Tallyra builds automation in stages on top of its current system to reach full automation thanks to Tallyra AI. It automates every manual task performed by the user. It starts by connecting to all sources of accounting</p></div>
  <div class="col3" style="left:131px"><div class="n">2</div><h4>Tallyra builds</h4><p>Tallyra builds automation in stages on top of its current system to reach full automation thanks to Tallyra AI. It automates every manual task performed by the user. It starts by connecting to all sources of accounting</p></div>
  <div class="col3" style="left:245px"><div class="n">3</div><h4>Tallyra builds</h4><p>Tallyra builds automation in stages on top of its current system to reach full automation thanks to Tallyra AI. It automates every manual task performed by the user. It starts by connecting to all sources of accounting</p></div>
  <div class="brand"><i></i>BRIXLEY</div><div class="rule"></div><div class="page">12</div>
</section>

<!-- Table -->
<section class="slide c1 r4">
  <div class="deco"></div>
  <div class="tag"></div><h2 class="title">YOUR HEADLINE HERE</h2><p class="sub">Lorem ipsum is simply dummy has been</p>
  <div class="txt" style="left:16px;top:54px;width:320px;font-size:4px;line-height:1.6">Tallyra builds automation in stages on top of its current system to reach full automation thanks to Tallyra AI. It automates every manual task performed by the user, starting with all sources of accounting data such as bank accounts and credit cards.</div>
  <table>
    <tr><th style="width:62%">Task</th><th>Weeks to Complete</th></tr>
    <tr><td>Discovery</td><td class="c">1-2</td></tr>
    <tr><td>Phase 1</td><td class="c">6-10</td></tr>
    <tr><td>Phase 2</td><td class="c">8-12</td></tr>
    <tr><td class="b">Total Number of Weeks</td><td></td></tr>
  </table>
  <div class="brand"><i></i>BRIXLEY</div><div class="rule"></div><div class="page">12</div>
</section>

<!-- Chart -->
<section class="slide c2 r4">
  <div class="deco"></div>
  <div class="tag"></div><h2 class="title">YOUR HEADLINE HERE</h2><p class="sub">Lorem ipsum is simply dummy has been</p>
  <svg style="position:absolute;left:16px;top:52px" width="180" height="112" viewBox="0 0 180 112" font-family="Open Sans, sans-serif" font-size="3.5" fill="#555">
    <g fill="#d92b2f">
      <rect x="4" y="48" width="12" height="51"/><rect x="18" y="37" width="12" height="62"/><rect x="32" y="58" width="12" height="41"/><rect x="46" y="76" width="12" height="23"/><rect x="60" y="77" width="12" height="22"/>
    </g>
    <g fill="#3f86d0">
      <rect x="74" y="90" width="12" height="9"/><rect x="88" y="80" width="12" height="19"/><rect x="102" y="75" width="12" height="24"/><rect x="116" y="52" width="12" height="47"/><rect x="130" y="44" width="12" height="55"/><rect x="144" y="18" width="12" height="81"/>
    </g>
    <line x1="2" y1="99" x2="160" y2="99" stroke="#999" stroke-width=".5"/>
    <g text-anchor="middle">
      <text x="10" y="46">120</text><text x="24" y="35">146</text><text x="38" y="56">96</text><text x="52" y="74">53</text><text x="66" y="75">50.5</text><text x="80" y="88">20.9</text><text x="94" y="78">44</text><text x="108" y="73">55</text><text x="122" y="50">109</text><text x="136" y="42">129</text><text x="150" y="16">189</text>
      <text x="10" y="105">Jan</text><text x="24" y="105">Febr</text><text x="38" y="105">March</text><text x="52" y="105">April</text><text x="66" y="105">May</text><text x="80" y="105">June</text><text x="94" y="105">July</text><text x="108" y="105">Aug</text><text x="122" y="105">Oct</text><text x="136" y="105">Nov</text><text x="150" y="105">Dec</text>
    </g>
  </svg>
  <div class="txt" style="left:212px;top:43px;width:130px;font-size:4.1px;line-height:1.6">
    Tallyra builds automation in stages on top of its current system to reach full automation thanks to Tallyra AI. It automates every manual task performed by the user. It starts by connecting to all sources of accounting data such as bank accounts, credit cards, webshops or document storage (Boxwell or Vaultly). Based on this data, it creates bookings and generates financial reports. Finally, a chat-like interface lets users communicate smoothly, so it acts as a trusted advisor for all their accounting queries.
    <em class="blue" style="margin-top:3px">Blockchain software license or<br>Token-as-a-License (TaaL)</em>
    It is possible to create tokens on a blockchain that represent software licenses, also known as Token-as-a-License (TaaL). Tallyra creates TaaL by
  </div>
  <div class="brand"><i></i>BRIXLEY</div><div class="rule"></div><div class="page">12</div>
</section>

<!-- Closing -->
<section class="slide c3 r4">
  <div class="close-band">
    <div class="brand"><i></i>BRIXLEY</div>
    <div class="sep"></div>
    <div class="info">T: +000 555 0142<br>T: +000 555 0142<br>E: hello@brixleymail.com<br>P.O. Box 1200, Harbour Lane<br>Westvale 0000, Australia</div>
  </div>
</section>

</body>
</html>
```